High End Notary Service Business Card Design

Want a professional and elegant/luxurious business card that is clean and simple in the design. A notary is a trusted professional that helps people sign very important documents. The card should be in alignment with this service provided.

Most of the time, service will be for the purchase of a home or refinance of a mortgage

There is NO LOGO. This is aesthetic. A look and feel. Conveying professionalism and concierge level of service.

Target Market(s)

Other business professionals, Lawyers, Escrow Officers, Loan Officers

Industry/Entity Type

Legal

Contact Information for Business Card

This will be a one-sided business card

Colors
35a7d7
3176b5
85cae6
d3a5cc
b868aa
ffffff
0356a4

Requirements
Must have
• Lorena T. Mirabel-Hodgkins
Notary Public

642-871-3094
MirabelSigningDesk@Wexmail.com
Nice to have
• Headshot photo below. Convey the aspect of signing documents. No black cards. Preference is shades of blue: light blue, navy, aqua, gold, white, or lavendar, etc.
Should not have
• No scales or legal scales.

```html
<!DOCTYPE html>
<html lang="en">
<head>
<meta charset="utf-8">
<title>Lorena T. Mirabel-Hodgkins — Notary Public</title>
<link rel="stylesheet" href="https://fonts.googleapis.com/css2?family=Libre+Franklin:wght@700;800;900&display=swap">
<style>
  :root {
    --navy: #0a0f5c;
    --rail-light: #d9dce3;
    --marble-a: #f7f8f9;
    --marble-b: #eceef0;
    --ink: #0b0b10;
    --white: #ffffff;
    --portrait-sky: #9fb0cc;
    --portrait-warm: #c9a07c;
  }
  * { margin: 0; padding: 0; box-sizing: border-box; }
  html, body { width: 686px; height: 1200px; overflow: hidden; }
  body {
    font-family: "Libre Franklin", "Arial Black", sans-serif;
    color: var(--ink);
  }
  .card {
    position: relative;
    width: 686px;
    height: 1200px;
    overflow: hidden;
    background:
      radial-gradient(ellipse at 75% 20%, var(--marble-b) 0%, transparent 45%),
      radial-gradient(ellipse at 20% 85%, var(--marble-b) 0%, transparent 40%),
      linear-gradient(160deg, var(--marble-a) 0%, #f1f2f4 50%, var(--marble-a) 100%);
  }
  .rail { position: absolute; background: var(--navy); }
  .rail::after {
    content: "";
    position: absolute;
    top: 0; bottom: 0;
    left: 9px; width: 10px;
    background: var(--rail-light);
  }
  .rail--top { left: 86px; top: 0; width: 57px; height: 366px; }
  .rail--bottom { left: 86px; top: 739px; width: 57px; height: 461px; }
  .portrait-frame {
    position: absolute;
    left: 86px; top: 357px;
    width: 220px; height: 272px;
    background: var(--navy);
  }
  .portrait {
    position: absolute;
    left: 9px; top: 9px; right: 1px; bottom: 1px;
    background:
      radial-gradient(ellipse at 50% 45%, var(--portrait-warm) 0%, transparent 42%),
      linear-gradient(180deg, var(--portrait-sky) 0%, #b7c3d6 60%, #a9b98a 100%);
  }
  .name {
    position: absolute;
    left: 86px; top: 650px;
    font-size: 35px;
    font-weight: 800;
    letter-spacing: -0.2px;
    white-space: nowrap;
  }
  .title {
    position: absolute;
    left: 87px; top: 698px;
    font-size: 23px;
    font-weight: 700;
  }
  .contact {
    position: absolute;
    left: 112px;
    display: flex;
    align-items: center;
    gap: 10px;
    font-weight: 800;
    white-space: nowrap;
  }
  .contact svg { flex: none; }
  .contact--phone { top: 787px; font-size: 33px; }
  .contact--email { top: 850px; font-size: 25px; }
</style>
</head>
<body>
  <main class="card">
    <div class="rail rail--top"></div>
    <div class="portrait-frame">
      <div class="portrait" role="img" aria-label="Headshot of the notary"></div>
    </div>

    <h1 class="name">Lorena T. Mirabel-Hodgkins</h1>
    <p class="title">Notary Public</p>

    <div class="rail rail--bottom"></div>

    <p class="contact contact--phone">
      <svg width="28" height="28" viewBox="0 0 24 24" aria-hidden="true">
        <path d="M6.6 10.8a15 15 0 0 0 6.6 6.6l2.2-2.2a1 1 0 0 1 1-.25 11.4 11.4 0 0 0 3.6.57 1 1 0 0 1 1 1V20a1 1 0 0 1-1 1A17 17 0 0 1 3 4a1 1 0 0 1 1-1h3.5a1 1 0 0 1 1 1c0 1.25.2 2.45.57 3.57a1 1 0 0 1-.25 1z" fill="var(--white)" stroke="var(--navy)" stroke-width="1"/>
        <path d="M14 3.5a7 7 0 0 1 6.5 6.5M14 7a3.5 3.5 0 0 1 3 3" fill="none" stroke="var(--white)" stroke-width="1.6" stroke-linecap="round"/>
      </svg>
      <span>642-871-3094</span>
    </p>
    <p class="contact contact--email">
      <svg width="32" height="22" viewBox="0 0 32 22" aria-hidden="true">
        <rect x="1" y="1" width="30" height="20" fill="var(--white)" stroke="var(--navy)" stroke-width="1"/>
        <path d="M1.5 1.5 16 12 30.5 1.5" fill="none" stroke="var(--navy)" stroke-width="1.6"/>
      </svg>
      <span>MirabelSigningDesk@Wexmail.com</span>
    </p>
  </main>
</body>
</html>
```